Vesit cards for web development company

We need a business card design for our company. The company develops online platforms and conducts marketing consulting. Company logo. The cards must fit in with us (a junior start UP), but they must also be professional enough to impress with investors like banks. We wish you a combination of classic and modern design

Target Market(s)

Business partners and IT and marketing customers

Industry/Entity Type

It Company

Contact Information for Business Card

Folgende Information müssen Drauf.
Name, Position, Telefon Nr., Mobile Nr., E-Mail adresse, Optional sind noch Webadresse und HRB Nummer

Colors

Designer to choose colors to be used in the design.

Requirements
Must have
• The cards have to fit into the logo later and have to be dynamic and serious at the same time

```html
<!DOCTYPE html>
<html lang="en">
<head>
<meta charset="utf-8">
<title>Kestrel Development – Business Card</title>
<link href="https://fonts.googleapis.com/css2?family=Roboto:wght@400;500;700&family=Roboto+Condensed:wght@700&display=swap" rel="stylesheet">
<style>
  :root {
    --backdrop: #2a2a2a;
    --paper: #f3f3f3;
    --brand-blue: #1272b8;
    --ink: #4a4a4a;
    --muted: #8a8a8a;
    --rule: #b5b5b5;
    --band-grey: #8c8c8c;
    --white: #ffffff;
  }
  * { margin: 0; padding: 0; box-sizing: border-box; }
  html, body { width: 1200px; height: 960px; overflow: hidden; }
  body {
    background: var(--backdrop);
    position: relative;
    font-family: "Roboto", Arial, sans-serif;
  }
  .card {
    position: absolute;
    width: 600px;
    height: 342px;
    border-radius: 20px;
    overflow: hidden;
  }
  /* Front */
  .card--front { left: 314px; top: 113px; background: var(--paper); }
  .wordmark {
    position: absolute;
    left: 0; right: 0; top: 170px;
    text-align: center;
    color: var(--brand-blue);
    font-family: "Roboto", Arial, sans-serif;
    font-weight: 700;
    line-height: 1;
  }
  .card--front .wordmark { top: 62px; }
  .wordmark__top { display: block; font-size: 46px; letter-spacing: 3px; }
  .wordmark__bottom { display: block; font-size: 32px; letter-spacing: 1px; margin-top: 8px; }
  .contact-row {
    position: absolute;
    left: 0; right: 0; top: 255px;
    height: 40px;
  }
  .contact-list { position: absolute; top: 1px; font-size: 14.5px; color: var(--ink); line-height: 19px; }
  .contact-list li { list-style: none; display: flex; align-items: center; gap: 8px; }
  .contact-list--phones { left: 46px; }
  .contact-list--web { right: 44px; text-align: right; }
  .contact-list--web li { justify-content: flex-end; }
  .icon { width: 12px; height: 14px; fill: var(--brand-blue); flex: none; }
  .divider { position: absolute; top: 0; width: 2px; height: 38px; background: var(--rule); }
  .divider--left { left: 188px; }
  .divider--right { left: 362px; }
  .person { position: absolute; left: 190px; width: 172px; text-align: center; top: -2px; }
  .person__name {
    font-family: "Roboto Condensed", "Arial Narrow", sans-serif;
    font-weight: 700; font-size: 22px; color: var(--brand-blue); line-height: 24px;
  }
  .person__role { font-size: 15px; font-weight: 500; color: var(--muted); line-height: 20px; }
  .band { position: absolute; bottom: 0; height: 8px; }
  .band--blue { left: 0; width: 494px; background: var(--brand-blue); }
  .band--grey { left: 496px; right: 0; background: var(--band-grey); }
  /* Back */
  .card--back { left: 311px; top: 472px; background: var(--brand-blue); border-radius: 22px; }
  .card--back .wordmark { top: 100px; color: var(--white); }
  .card--back .wordmark__top { font-size: 72px; letter-spacing: 6px; }
  .website {
    position: absolute; left: 0; right: 0; top: 288px;
    text-align: center; color: var(--white);
    font-size: 15px; letter-spacing: 5.2px;
  }
</style>
</head>
<body>
  <section class="card card--front">
    <div class="wordmark">
      <span class="wordmark__top">KESTREL</span>
      <span class="wordmark__bottom">DEVELOPMENT</span>
    </div>
    <div class="contact-row">
      <ul class="contact-list contact-list--phones">
        <li>
          <svg class="icon" viewBox="0 0 12 14" aria-hidden="true"><path d="M2.5 0.5 L4.5 0.5 L5.3 3.6 L3.9 4.6 Q5 7.6 7.6 9.6 L8.8 8.3 L11.8 9.3 L11.8 11.4 Q11.6 13.2 9.6 13 Q1 11.8 0.4 2.6 Q0.4 0.6 2.5 0.5 Z"/></svg>
          <span>614 552 0871</span>
        </li>
        <li>
          <svg class="icon" viewBox="0 0 12 14" aria-hidden="true"><path d="M3 0 H9 Q10.5 0 10.5 1.5 V12.5 Q10.5 14 9 14 H3 Q1.5 14 1.5 12.5 V1.5 Q1.5 0 3 0 Z M3 2 V10.5 H9 V2 Z M6 11.3 A0.9 0.9 0 1 0 6.01 11.3 Z"/></svg>
          <span>614 903 2746</span>
        </li>
      </ul>
      <span class="divider divider--left"></span>
      <div class="person">
        <p class="person__name">LUKAS BRENNER</p>
        <p class="person__role">CEO/FOUNDER</p>
      </div>
      <span class="divider divider--right"></span>
      <ul class="contact-list contact-list--web">
        <li>
          <span>hello@kestrel.io</span>
          <svg class="icon" viewBox="0 0 14 14" style="width:14px" aria-hidden="true"><path d="M1 3 H13 V11.5 H1 Z M1.8 3.8 L7 8 L12.2 3.8 Z" fill-rule="evenodd"/></svg>
        </li>
        <li>
          <span>www.kestrel.io</span>
          <svg class="icon" viewBox="0 0 14 14" style="width:14px" aria-hidden="true"><circle cx="7" cy="7" r="6.2"/><path d="M4 3.5 Q6 4.5 5.5 6.5 Q4 7.5 4.6 10 M8.5 2.2 Q9 4 10.8 4.2 M8 8.5 Q9.5 8 10 10.5" stroke="#f3f3f3" stroke-width="1.1" fill="none"/></svg>
        </li>
      </ul>
    </div>
    <span class="band band--blue"></span>
    <span class="band band--grey"></span>
  </section>

  <section class="card card--back">
    <div class="wordmark">
      <span class="wordmark__top">KESTREL</span>
    </div>
    <p class="website">www.kestreldevelopment.com</p>
  </section>
</body>
</html>
```